New, modern business card for growing audiology practice

We need a new business card for our audiology practice. Our logo and website have recently changed (more modern) and we want our business cards to reflect this change.
We conduct hearing tests, perform earwax removals, and fit & dispense hearing aids to our patients. We are a family owned practice in which the owner is the one who works directly with the patient. I have attached logos in various formats to use, as well as two ideas I found on this website; as well as a scanned copy of our current logo. Good luck!

Industry/Entity Type

Business

Contact Information for Business Card

Company name: Birchmont Hearing Center
Provider name: Peter Lowsby, Au.D. F/NSO
Phone number: (555) 318-6042
Address: 287 W. Hollister Rd. Maple Ridge, OH 40000
email: birchmonthearing@quillpost.net
website: birchmonthearing.net

Colors
000000
aaaaaa
dbdbdb
cacaca
9bcb3c
afd23c
cadf82
b1b1b1

Requirements
Must have
• My card must include information in the "details" section. In the attached images, I found a few that I liked and I would like to model after - "steady strivin'" and "Sound Lab Clinic".
• Must be horizontal.
• Must include logos provided. I uploaded them in various file formats and various ways.
• Must match logo font, if possible, if not, please get as close as you can.
Nice to have
• I really like the idea of having a color on one side with just the logo and company name and the contact information and provider name on the other side. I also really like the idea of having the main color dominating on the logo/company side with accent of that same color on the contact side of the card.
Should not have
• Must not be vertical.

```html
<!DOCTYPE html>
<html lang="en">
<head>
<meta charset="utf-8">
<title>Birchmont Hearing Center – Business Card</title>
<link rel="stylesheet" href="https://fonts.googleapis.com/css2?family=Lato:wght@400&family=Oswald:wght@500&family=Work+Sans:wght@300;400&display=swap">
<style>
  :root {
    --stage: #2b2b2b;
    --card: #0d0d0d;
    --card-edge: #161616;
    --green: #afd23c;
    --green-deep: #9bcb3c;
    --white: #f2f2f2;
    --grey: #cacaca;
  }
  * { box-sizing: border-box; margin: 0; padding: 0; }
  html, body {
    width: 1200px; height: 900px; overflow: hidden;
    background: var(--stage);
  }
  .canvas {
    position: relative; width: 1200px; height: 900px;
    display: flex; flex-direction: column; align-items: center; justify-content: center; gap: 30px;
  }
  .card {
    position: relative; width: 700px; height: 400px;
    background: linear-gradient(160deg, var(--card-edge), var(--card));
    box-shadow: 0 12px 30px rgba(0,0,0,.45);
    overflow: hidden;
  }
  .card::after {
    content: ""; position: absolute; left: 0; right: 0; bottom: 0; height: 7px;
    background: var(--green);
  }
  .brand {
    display: flex; align-items: center; justify-content: center; gap: 14px;
    font-family: "Lato", sans-serif; font-weight: 400;
    color: var(--white); text-transform: uppercase; letter-spacing: 1.5px;
    white-space: nowrap;
  }
  .brand-dot { width: 16px; height: 16px; border-radius: 50%; background: var(--green); }
  .card--front .brand { position: absolute; left: 0; right: 0; top: 168px; font-size: 30px; }
  .web {
    font-family: "Work Sans", sans-serif; font-weight: 300; color: var(--white);
    white-space: nowrap;
  }
  .web .accent { color: var(--green); font-weight: 400; }
  .card--front .web { position: absolute; left: 0; right: 0; bottom: 34px; text-align: center; font-size: 19px; }

  .card--back .brand { position: absolute; left: 0; right: 0; top: 52px; font-size: 30px; }
  .details {
    position: absolute; top: 170px; left: 20px; right: 20px;
    display: flex; align-items: center; justify-content: center;
  }
  .provider { text-align: right; padding-right: 20px; white-space: nowrap; }
  .provider-name {
    font-family: "Oswald", sans-serif; font-weight: 500; font-size: 27px;
    color: var(--green); text-transform: uppercase; letter-spacing: 0; line-height: 1.15;
  }
  .provider-role {
    font-family: "Work Sans", sans-serif; font-weight: 300; font-size: 16px; color: var(--white);
  }
  .divider { width: 2px; height: 74px; background: var(--green-deep); flex: none; }
  .contact { list-style: none; padding-left: 20px; }
  .contact li {
    display: flex; align-items: center; gap: 12px;
    font-family: "Work Sans", sans-serif; font-weight: 300; font-size: 16.5px; color: var(--white);
    line-height: 1.4; white-space: nowrap;
  }
  .contact svg { width: 13px; height: 13px; flex: none; }
  .address {
    position: absolute; left: 0; right: 0; bottom: 48px; text-align: center;
    font-family: "Work Sans", sans-serif; font-weight: 300; font-size: 20px; color: var(--white);
    letter-spacing: .3px; white-space: nowrap;
  }
</style>
</head>
<body>
<main class="canvas">
  <section class="card card--front" aria-label="Card front">
    <div class="brand"><span class="brand-dot"></span><span>Birchmont Hearing Center</span></div>
    <p class="web">www.<span class="accent">birchmonthearing</span>.net</p>
  </section>

  <section class="card card--back" aria-label="Card back">
    <div class="brand"><span class="brand-dot"></span><span>Birchmont Hearing Center</span></div>
    <div class="details">
      <div class="provider">
        <p class="provider-name">Peter Lowsby, Au.D. F/NSO</p>
        <p class="provider-role">Owner-Audiologist</p>
      </div>
      <div class="divider"></div>
      <ul class="contact">
        <li>
          <svg viewBox="0 0 16 16" aria-hidden="true"><path fill="var(--green)" d="M3.6 1.2l2.3 2.6-1.3 1.8c.9 2 2.4 3.5 4.4 4.4l1.8-1.3 2.6 2.3-1.2 2.3C7 13.1 2.9 9 1.3 3.4z"/></svg>
          (555) 318-6042
        </li>
        <li>
          <svg viewBox="0 0 16 16" aria-hidden="true"><rect x="1.5" y="3.5" width="13" height="9" fill="none" stroke="var(--green)" stroke-width="1.5"/><path d="M1.5 3.5 8 9l6.5-5.5" fill="none" stroke="var(--green)" stroke-width="1.5"/></svg>
          birchmonthearing@quillpost.net
        </li>
        <li>
          <svg viewBox="0 0 16 16" aria-hidden="true"><g fill="none" stroke="var(--green)" stroke-width="1.3"><circle cx="8" cy="8" r="6.3"/><ellipse cx="8" cy="8" rx="2.8" ry="6.3"/><path d="M1.7 8h12.6M2.6 4.8h10.8M2.6 11.2h10.8"/></g></svg>
          <span class="web">www.<span class="accent">birchmonthearing</span>.net</span>
        </li>
      </ul>
    </div>
    <p class="address">287 W. Hollister Rd. Maple Ridge, OH 40000</p>
  </section>
</main>
</body>
</html>
```